Fun Trendy High End Spa Services
Business Card, Gift Certificate, Gift Certificate Envelope
I need double sided standard sized Business Card [3.5" x 2"]
We like what is in logo that was uploaded but please use your creativity. We are open to any ideas.
Simple
Lena Harbus LMT
Owner
Mobile
BP@BrightPebblo.com
BrightPebblo.com
We are open to all concepts. So please be creative. This is for Very high end spa service so it needs to look very good. We thought black paper for a base on business cards, gift certificate and GC envelope but are open to any and all ideas! Thank You! We will pick a winner early if we find the perfect design.
"The greatest wealth is health"
(Doesnt need " " on there just use your own idea and play with it.)
Here is The winning logo design. We really like the style but please feel free to be creative with it! Thank you so much!
This is the style of gift certificate that we want designed to match our business card.

```html
<!DOCTYPE html>
<html lang="en">
<head>
<meta charset="utf-8">
<title>Bright Pebblo – Business Card</title>
<link rel="stylesheet" href="https://fonts.googleapis.com/css2?family=Questrial&family=Cormorant+Garamond:ital,wght@1,500&display=swap">
<style>
  :root {
    --page: #ffffff;
    --card-dark: #121212;
    --card-mid: #242424;
    --grain-light: rgba(255,255,255,0.035);
    --grain-dark: rgba(0,0,0,0.25);
    --silver: #d6d6d6;
    --silver-dim: #a0a0a0;
    --pink: #e0457f;
    --white: #f2f2f2;
    --band-light: #9a9a9a;
    --band-dark: #262626;
  }
  * { margin: 0; padding: 0; box-sizing: border-box; }
  html, body { width: 1200px; height: 847px; overflow: hidden; background: var(--page); }
  .canvas { position: relative; width: 1200px; height: 847px; }

  .card {
    position: absolute;
    left: 329px;
    width: 542px;
    height: 306px;
    border-radius: 24px;
    overflow: hidden;
    font-family: "Questrial", sans-serif;
    color: var(--white);
    background:
      radial-gradient(circle at 18% 22%, var(--grain-light), transparent 22%),
      radial-gradient(circle at 72% 64%, var(--grain-light), transparent 26%),
      radial-gradient(circle at 46% 86%, var(--grain-dark), transparent 30%),
      radial-gradient(circle at 88% 18%, var(--grain-dark), transparent 24%),
      radial-gradient(ellipse at 45% 35%, var(--card-mid), var(--card-dark) 78%);
  }
  .card-front { top: 101px; }
  .card-back { top: 452px; }

  /* front */
  .brand {
    position: absolute;
    left: 40px;
    top: 38px;
    display: flex;
    align-items: center;
    gap: 14px;
  }
  .brand-dot {
    width: 40px; height: 40px;
    border: 3px solid var(--silver);
    border-radius: 50%;
  }
  .brand-name {
    font-size: 31px;
    line-height: 29px;
    color: var(--silver);
    letter-spacing: 1px;
  }
  .contact { position: absolute; left: 42px; top: 146px; }
  .person { font-size: 23px; line-height: 26px; color: var(--pink); }
  .person .credential { font-size: 15px; color: var(--white); }
  .role { font-size: 16px; line-height: 21px; color: var(--silver-dim); }
  .lines { margin-top: 10px; font-size: 14px; line-height: 19px; color: var(--white); letter-spacing: 0.4px; }
  .lines span { display: inline-block; width: 24px; }
  .motto-band {
    position: absolute;
    left: 240px;
    right: 0;
    top: 230px;
    height: 26px;
    background: linear-gradient(to bottom, var(--band-light), var(--band-dark));
    font-size: 17px;
    line-height: 26px;
    padding-left: 10px;
    color: var(--white);
  }

  /* back */
  .back-brand {
    position: absolute;
    left: 0; right: 0;
    top: 100px;
    display: flex;
    justify-content: center;
    align-items: center;
    gap: 12px;
    font-size: 30px;
    color: var(--silver);
    letter-spacing: 1px;
  }
  .back-brand .brand-dot { width: 34px; height: 34px; }
  .back-tagline {
    position: absolute;
    left: 0; right: 0;
    top: 186px;
    text-align: center;
    font-family: "Cormorant Garamond", serif;
    font-style: italic;
    font-weight: 500;
    font-size: 29px;
    color: var(--silver);
  }
  .back-band {
    position: absolute;
    left: 0; right: 0;
    top: 236px;
    height: 16px;
    background: linear-gradient(to right, transparent, #6a6a6a 30%, #7c7c7c 50%, #6a6a6a 70%, transparent);
    opacity: 0.6;
  }
</style>
</head>
<body>
<main class="canvas">
  <section class="card card-front" role="img" aria-label="Front of business card on black leather-textured paper">
    <div class="brand">
      <div class="brand-dot"></div>
      <div class="brand-name">Bright<br>Pebblo</div>
    </div>
    <div class="contact">
      <p class="person">Lena Harbus <span class="credential">LMT</span></p>
      <p class="role">Owner</p>
      <p class="lines"><span>P :</span>555-014-2271<br><span>E:</span>BP@BrightPebblo.com<br><span>W:</span>BrightPebblo.com</p>
    </div>
    <div class="motto-band">The greatest wealth is health</div>
  </section>

  <section class="card card-back" role="img" aria-label="Back of business card on black leather-textured paper">
    <div class="back-brand"><div class="brand-dot"></div>Bright Pebblo</div>
    <p class="back-tagline">Luxury in Home Spa Experience</p>
    <div class="back-band"></div>
  </section>
</main>
</body>
</html>
```